BEACON CABS

Taxi card design

Need changes very slow in replying to my messages.

Target Market(s)

Customers

Industry/Entity Type

Taxi

Contact Information for Business Card

See previous design

Font styles to use
Sans Serif

Colors
A7469A
B969AE
D3A5CF
EDDBEB
F8F0F9
6B429C
8869AF
B7A5CE
E3DAEB
F3F0F8

Requirements
Nice to have
• We are in the business of looking after people, not just driving vehicles front
Should not have
• Front number 01632 480 480 needs to big big

```html
<!DOCTYPE html>
<html lang="en">
<head>
<meta charset="utf-8">
<title>Beacon Cabs – Business Card</title>
<link rel="stylesheet" href="https://fonts.googleapis.com/css2?family=Montserrat:wght@400;500;600;700;800&display=swap">
<style>
  :root {
    --page-bg: #2a2a2c;
    --card-bg: #151515;
    --white: #ffffff;
    --text-soft: #e8e8e8;
    --silver: #c4c4c4;
    --magenta: #a7469a;
    --magenta-light: #b969ae;
    --violet: #6b429c;
    --violet-light: #8869af;
  }
  * { box-sizing: border-box; margin: 0; padding: 0; }
  html, body {
    width: 1200px; height: 900px; overflow: hidden;
    background: var(--page-bg);
    font-family: "Montserrat", sans-serif;
  }
  .sheet {
    width: 1200px; height: 900px;
    display: flex; flex-direction: column; align-items: center; justify-content: center;
    gap: 44px;
  }
  .card {
    position: relative;
    width: 700px; height: 400px;
    background: var(--card-bg);
    box-shadow: 0 18px 40px rgba(0,0,0,.45);
    overflow: hidden;
  }
  .card__stripe {
    position: absolute; left: 0; right: 0; bottom: 34px; height: 6px;
    background: linear-gradient(90deg, var(--magenta), var(--magenta-light) 45%, var(--violet-light) 75%, var(--violet));
  }

  /* Front */
  .brand {
    position: absolute; left: 48px; top: 120px; width: 260px;
  }
  .brand__name {
    display: flex; align-items: center; gap: 10px;
    font-weight: 800; font-size: 34px; letter-spacing: .5px; color: var(--white);
    line-height: 1;
  }
  .brand__mark {
    width: 14px; height: 14px; background: var(--magenta); flex: none;
  }
  .brand__service {
    margin-top: 14px; margin-left: 24px;
    font-weight: 700; font-size: 17px; color: var(--white);
  }
  .divider {
    position: absolute; left: 330px; top: 70px; width: 1.5px; height: 230px;
    background: var(--magenta);
  }
  .contact {
    position: absolute; left: 360px; top: 66px; right: 30px;
    color: var(--text-soft);
  }
  .contact__name {
    font-weight: 700; font-size: 22px; letter-spacing: .5px;
    color: var(--magenta-light); text-transform: uppercase;
  }
  .contact__role { font-size: 15px; font-weight: 500; margin-top: 3px; color: var(--white); }
  .contact__address { font-size: 14px; line-height: 1.45; margin-top: 14px; }
  .contact__list { list-style: none; margin-top: 14px; }
  .contact__item {
    display: flex; align-items: center; gap: 10px;
    font-size: 14px; line-height: 1.3; margin-top: 7px;
  }
  .contact__item--phone { font-size: 24px; font-weight: 700; color: var(--white); letter-spacing: .5px; }
  .contact__icon { width: 16px; height: 16px; flex: none; fill: var(--magenta-light); }
  .contact__item--phone .contact__icon { width: 20px; height: 20px; }

  /* Back */
  .back-brand {
    position: absolute; left: 0; right: 0; top: 120px;
    display: flex; align-items: center; justify-content: center; gap: 16px;
    font-weight: 800; font-size: 68px; letter-spacing: 1px; color: var(--silver);
    line-height: 1;
  }
  .back-brand__mark { width: 26px; height: 26px; background: var(--silver); flex: none; }
  .services {
    position: absolute; left: 0; right: 0; bottom: 62px;
    text-align: center; font-size: 16px; font-weight: 500; letter-spacing: 1.5px;
    color: var(--white); text-transform: uppercase;
  }
  .services__dot { color: var(--magenta); margin: 0 12px; }
</style>
</head>
<body>
<main class="sheet">
  <section class="card card--front" aria-label="Business card front">
    <div class="brand">
      <div class="brand__name"><span class="brand__mark"></span>BEACON CABS</div>
      <div class="brand__service">24/7 Service</div>
    </div>
    <div class="divider"></div>
    <div class="contact">
      <h1 class="contact__name">Mark Hollins</h1>
      <p class="contact__role">President</p>
      <p class="contact__address">Mill Lane Chapel Hall<br>Foundry St, Ashby<br>AB12 3CD</p>
      <ul class="contact__list">
        <li class="contact__item contact__item--phone">
          <svg class="contact__icon" viewBox="0 0 24 24" aria-hidden="true"><path d="M6.6 10.8a15.1 15.1 0 0 0 6.6 6.6l2.2-2.2c.3-.3.7-.4 1-.2 1.1.4 2.3.6 3.6.6.6 0 1 .4 1 1V20c0 .6-.4 1-1 1A17 17 0 0 1 3 4c0-.6.4-1 1-1h3.5c.6 0 1 .4 1 1 0 1.3.2 2.5.6 3.6.1.3 0 .7-.2 1z"/></svg>
          01632 480 480
        </li>
        <li class="contact__item">
          <svg class="contact__icon" viewBox="0 0 24 24" aria-hidden="true"><path d="M3 5h18v14H3z M3 5l9 7 9-7" fill="none" stroke="currentColor"/><path d="M3 5h18v2l-9 7-9-7z M3 9l9 7 9-7v10H3z"/></svg>
          beaconcabs@mailbox.co.uk
        </li>
        <li class="contact__item">
          <svg class="contact__icon" viewBox="0 0 24 24" aria-hidden="true"><path d="M12 2a10 10 0 1 0 0 20 10 10 0 0 0 0-20zm6.9 6h-3a15.7 15.7 0 0 0-1.4-3.6A8 8 0 0 1 18.9 8zM12 4c.8 1.2 1.5 2.5 1.9 4h-3.8c.4-1.5 1.1-2.8 1.9-4zM4.3 14a8.2 8.2 0 0 1 0-4h3.4a16.5 16.5 0 0 0 0 4zm.8 2h3a15.7 15.7 0 0 0 1.4 3.6A8 8 0 0 1 5.1 16zm3-8h-3a8 8 0 0 1 4.4-3.6C8.9 5.5 8.4 6.7 8.1 8zM12 20c-.8-1.2-1.5-2.5-1.9-4h3.8c-.4 1.5-1.1 2.8-1.9 4zm2.3-6H9.7a14.7 14.7 0 0 1 0-4h4.6a14.7 14.7 0 0 1 0 4zm.2 5.6c.6-1.1 1.1-2.3 1.4-3.6h3a8 8 0 0 1-4.4 3.6zm1.8-5.6a16.5 16.5 0 0 0 0-4h3.4a8.2 8.2 0 0 1 0 4z"/></svg>
          www.beaconcabs.co.uk
        </li>
      </ul>
    </div>
    <div class="card__stripe"></div>
  </section>

  <section class="card card--back" aria-label="Business card back">
    <div class="back-brand"><span class="back-brand__mark"></span>BEACON CABS</div>
    <p class="services">Airport Transfers<span class="services__dot">•</span>Minibuses<span class="services__dot">•</span>School Transport</p>
    <div class="card__stripe"></div>
  </section>
</main>
</body>
</html>
```